New Stationery New Logo for KT Fabrication Limited

We have a new logo and now want new stationary to go with it

This will be

Letterhead
Compliments Slip
Business Cards

Company details are
KT Fabrication Limited
Dellmoor Road, Hallowford, Eastmere, CV34 7HX, UK
Telephone : +44(0)1788 390617
Fax: +44(0)1788 473928
Email: sales@ktfabrication.co.uk
Web: www.ktfabrication.co.uk

Target Market(s)

Engineering / Metal Stamping

Industry/Entity Type

Manufacture

Contact Information for Business Card

Colin Brearley
Business Development Manager
KT Fabrication Limited
Dellmoor Road
Hallowford
Eastmere
CV34 7HX, UK

T: +44(0)1788 390617
F: +44(0)1788 473928
E: sales@ktfabrication.co.uk
W: www.ktfabrication.co.uk

Font styles to use
Sans Serif

Colors
33a6d7
0555a3
3176b5
85cae6
85acd3

Requirements
Must have
• Logo

```html
<!DOCTYPE html>
<html lang="en">
<head>
<meta charset="utf-8">
<title>KT Fabrication Limited – Stationery</title>
<link rel="stylesheet" href="https://fonts.googleapis.com/css2?family=Questrial&family=Montserrat:wght@600;700&family=Pinyon+Script&display=swap">
<style>
  :root {
    --blue-deep: #0555a3;
    --blue-mid: #3176b5;
    --blue-soft: #85acd3;
    --ink: #2b2b2b;
    --paper: #f7f7f7;
    --band: #3b3b3d;
    --card-dark: #48484a;
    --backdrop: #c8c8ca;
    --fold: #bdbdbd;
  }
  * { margin: 0; padding: 0; box-sizing: border-box; }
  html, body { width: 1200px; height: 838px; overflow: hidden; }
  body {
    background: radial-gradient(ellipse at 50% 40%, #dadadc 0%, var(--backdrop) 75%);
    font-family: "Questrial", sans-serif;
    color: var(--ink);
    position: relative;
  }
  .sheet {
    position: absolute;
    background: var(--paper);
    box-shadow: 0 2px 6px rgba(0,0,0,.22);
    overflow: hidden;
  }
  .brand {
    position: absolute;
    font-family: "Questrial", sans-serif;
    color: var(--blue-deep);
    letter-spacing: .32em;
    white-space: nowrap;
    display: flex;
    align-items: center;
    gap: .5em;
  }
  .brand-dot {
    width: .55em; height: .55em;
    border-radius: 50%;
    background: var(--blue-deep);
    display: inline-block;
  }
  .band {
    position: absolute; left: 0; right: 0; bottom: 0;
    background: var(--band);
  }
  .band-web {
    position: absolute; top: 0; bottom: 0;
    background: var(--blue-deep);
    border-left: 2px solid #fff;
    border-right: 2px solid #fff;
    color: #fff;
    display: flex; align-items: center; justify-content: center;
    font-size: 6.5px;
  }
  .contact-list { position: absolute; list-style: none; font-size: 6.6px; line-height: 9.2px; }
  .contact-list li { display: flex; align-items: center; gap: 4px; white-space: nowrap; }
  .icon {
    width: 6px; height: 6px; border-radius: 1px;
    background: var(--blue-deep);
    display: inline-block; flex: none;
  }
  .address { position: absolute; font-size: 6.6px; line-height: 9px; white-space: nowrap; }
  .label-envelope {
    position: absolute; left: 614px; top: 22px;
    font-size: 15px; color: #a9a9ab;
  }

  /* letterhead */
  .letterhead { left: 46px; top: 54px; width: 516px; height: 728px; }
  .letterhead .brand { left: 44px; top: 100px; font-size: 13px; }
  .letterhead .contact-list { left: 378px; top: 51px; }
  .letterhead .address { left: 378px; top: 93px; }
  .fold { position: absolute; left: 0; width: 15px; height: 1px; background: var(--fold); }
  .letter-body { position: absolute; left: 44px; top: 248px; width: 430px; font-size: 7.1px; line-height: 9.3px; text-align: justify; }
  .letter-body .salutation { font-family: "Montserrat", sans-serif; font-weight: 600; margin-bottom: 9px; }
  .letter-body p { margin-bottom: 9.3px; }
  .sign-off { position: absolute; left: 44px; top: 470px; font-size: 7.1px; line-height: 9.3px; }
  .sign-off strong { font-family: "Montserrat", sans-serif; font-weight: 600; }
  .signature { position: absolute; left: 112px; top: 458px; width: 106px; height: 56px; background: linear-gradient(90deg, #e6eaf3, #d9e0ef); border-radius: 3px; }
  .letterhead .band { height: 13px; }
  .letterhead .band-web { left: 352px; width: 124px; }

  /* envelope */
  .envelope { left: 614px; top: 54px; width: 540px; height: 270px; }
  .envelope .brand { left: 30px; top: 82px; font-size: 13px; }
  .envelope .address { left: 76px; top: 107px; text-align: center; }
  .envelope .band { height: 12px; }
  .envelope .band-web { left: 51px; width: 122px; }

  /* compliments slip */
  .slip { left: 614px; top: 372px; width: 516px; height: 244px; }
  .slip .brand { left: 25px; top: 71px; font-size: 12.5px; }
  .slip-greeting {
    position: absolute; left: 25px; top: 152px;
    font-family: "Pinyon Script", cursive; font-size: 19px; color: var(--blue-mid);
  }
  .slip .address { left: 25px; top: 189px; }
  .slip .contact-list { left: 108px; top: 189px; }
  .slip .band { height: 14px; }
  .slip .band-web { left: 354px; width: 124px; }

  /* business cards */
  .card-front { left: 614px; top: 661px; width: 222px; height: 122px; }
  .card-front .brand { left: 14px; top: 84px; font-size: 6.5px; letter-spacing: .28em; }
  .card-divider { position: absolute; left: 115px; top: 30px; width: 1px; height: 60px; background: #cfcfcf; }
  .card-person { position: absolute; left: 127px; top: 30px; }
  .card-name { font-family: "Montserrat", sans-serif; font-weight: 700; font-size: 6.3px; color: var(--blue-deep); letter-spacing: .04em; }
  .card-role { font-size: 5px; margin-top: 1px; }
  .card-front .contact-list { left: 127px; top: 51px; font-size: 4.8px; line-height: 6.8px; }
  .card-front .contact-list .icon { width: 4.5px; height: 4.5px; }
  .card-front .address { left: 127px; top: 80px; font-size: 4.8px; line-height: 6.6px; }
  .card-front .band { height: 8px; }
  .card-front .band-web { left: 21px; width: 79px; }

  .card-back { left: 887px; top: 661px; width: 222px; height: 122px; background: var(--card-dark); }
  .card-back .brand { left: 0; right: 0; top: 51px; justify-content: center; font-size: 10px; color: #fff; }
  .card-back .brand-dot { background: var(--blue-soft); }
  .card-back-web { position: absolute; left: 0; right: 0; top: 97px; text-align: center; font-size: 5px; color: #e4e4e4; }
</style>
</head>
<body>

<div class="label-envelope">envelope</div>

<!-- Letterhead -->
<section class="sheet letterhead" aria-label="Letterhead">
  <div class="brand"><span class="brand-dot"></span>KT FABRICATION</div>
  <ul class="contact-list">
    <li><span class="icon"></span>+44(0)1632 390617</li>
    <li><span class="icon"></span>+44(0)1632 473928</li>
    <li><span class="icon"></span>sales@ktfabrication.co.uk</li>
    <li><span class="icon"></span>www.ktfabrication.co.uk</li>
  </ul>
  <p class="address">Dellmoor Road, Hallowford<br>Eastmere, CV34 7HX, UK</p>

  <span class="fold" style="top:257px"></span>
  <span class="fold" style="top:363px"></span>
  <span class="fold" style="top:514px"></span>

  <div class="letter-body">
    <p class="salutation">Dear sir,</p>
    <p>Communication is a very integral part of living creatures, animals and humans. Communication may be verbal or written. Written communication however is only applicable to human beings. Can you even imagine a world without communication? Verbal communication can be through telephones, webcams or in person. Written communication is through letters, emails and mobile phone messages.</p>
    <p>In today’s world of great inventions and technology, letters have somehow become redundant. It is the time for text messages or chats. But they still can communicate a lot more than all other modes of communication. Organizations and various government departments still bank on letters as a strong medium of communication. There is no comparison in costs of sending letters as compared to costs of mobile phone messages though – letters are far cheaper. Letters now commonly known as “hard copy documents” are considered more relevant and important than email copies of text messages as proof or evidence of some sort.</p>
    <p>Letters speak volumes about a person or an organization that writes it. So one must take utmost care ensuring that the language used in any letter is appropriate for the occasion for which it is being written. Since a letter is also a written proof or document, if there are certain things that should not form a part of it, then that too should be carefully handled.</p>
    <p>Writing a good letter is an art. But if for some reason someone is unable to write that perfect letter, these different types of letters provide a base for you to build on. Sample letters have been given for everyone to understand what all information needs to form a part of the letter type and then it can be customized.</p>
  </div>
  <p class="sign-off">Yours Sincerely,<br><strong>Dana Whitcombe</strong></p>
  <div class="signature" role="img" aria-label="Handwritten signature in blue ink"></div>

  <div class="band"><div class="band-web">www.ktfabrication.co.uk</div></div>
</section>

<!-- Envelope -->
<section class="sheet envelope" aria-label="Envelope">
  <div class="brand"><span class="brand-dot"></span>KT FABRICATION</div>
  <p class="address">Dellmoor Road, Hallowford<br>Eastmere, CV34 7HX, UK</p>
  <div class="band"><div class="band-web">www.ktfabrication.co.uk</div></div>
</section>

<!-- Compliments slip -->
<section class="sheet slip" aria-label="Compliments slip">
  <div class="brand"><span class="brand-dot"></span>KT FABRICATION</div>
  <p class="slip-greeting">With Compliments</p>
  <p class="address">Dellmoor Road, Hallowford<br>Eastmere<br>CV34 7HX, UK</p>
  <ul class="contact-list">
    <li><span class="icon"></span>+44(0)1632 390617</li>
    <li><span class="icon"></span>+44(0)1632 473928</li>
    <li><span class="icon"></span>sales@ktfabrication.co.uk</li>
  </ul>
  <div class="band"><div class="band-web">www.ktfabrication.co.uk</div></div>
</section>

<!-- Business card front -->
<section class="sheet card-front" aria-label="Business card front">
  <div class="brand"><span class="brand-dot"></span>KT FABRICATION</div>
  <span class="card-divider"></span>
  <div class="card-person">
    <p class="card-name">PRIYA LOCKHART</p>
    <p class="card-role">General Manager</p>
  </div>
  <ul class="contact-list">
    <li><span class="icon"></span>+44(0)1632 390617</li>
    <li><span class="icon"></span>+44(0)1632 473928</li>
    <li><span class="icon"></span>sales@ktfabrication.co.uk</li>
    <li><span class="icon"></span>www.ktfabrication.co.uk</li>
  </ul>
  <p class="address">Dellmoor Road, Hallowford<br>Eastmere, CV34 7HX, UK</p>
  <div class="band"><div class="band-web"></div></div>
</section>

<!-- Business card back -->
<section class="sheet card-back" aria-label="Business card back">
  <div class="brand"><span class="brand-dot"></span>KT FABRICATION</div>
  <p class="card-back-web">www.ktfabrication.co.uk</p>
</section>

</body>
</html>
```